Dialysis Brochure

12 pages booklet, horizontal, 9 inches width x 6 inches high , luxury look
Updates

Landscape booklet 9 x 6

Need extra days to review

Target Market(s)

General public

Industry/Entity Type

Health Care

Colors

Designer to choose colors to be used in the design.

Requirements
Nice to have
• foil effect or similar

```html
<!DOCTYPE html>
<html lang="en">
<head>
<meta charset="utf-8">
<title>Harborview Renal Care Center – Dialysis Brochure</title>
<link href="https://fonts.googleapis.com/css2?family=Open+Sans:wght@300;400;600;700&display=swap" rel="stylesheet">
<style>
:root{
  --blue:#2f9fe0;
  --blue-dark:#1f86c8;
  --magenta:#d42a6f;
  --ink:#5b5f66;
  --ink-light:#8a8f96;
  --paper:#ffffff;
  --backdrop:#9c9c9c;
  --photo-a:#e9edf1;
  --photo-b:#c9d2da;
  --rule:#e3e6ea;
}
*{box-sizing:border-box;margin:0;padding:0}
html,body{width:1200px;height:3484px;overflow:hidden}
body{background:var(--backdrop);font-family:"Open Sans",Arial,sans-serif;color:var(--ink);position:relative}
.photo{position:absolute;background:linear-gradient(160deg,var(--photo-a),var(--photo-b))}
.photo.warm{background:linear-gradient(160deg,#f1e6dc,#c9b9a8)}
.photo.beach{background:linear-gradient(180deg,#cfe3ef 0%,#e7ddd0 55%,#d8c6b4 100%)}
.photo.round{border-radius:50%;border:4px solid #fff}
.photo.map{background:linear-gradient(180deg,#f3f3f1,#e6e7e4)}

.cover{position:absolute;left:250px;top:40px;width:700px;height:467px;background:var(--paper);overflow:hidden}
.cover .photo{left:0;top:70px;width:700px;height:290px}
.cover-tag{position:absolute;right:36px;top:14px;text-align:right;font-weight:300;font-size:22px;line-height:1.05;color:var(--ink-light)}
.cover-tag strong{display:block;font-weight:700;font-size:27px;color:var(--magenta)}
.cover-band{position:absolute;left:0;right:0;bottom:0;height:107px;background:var(--blue);color:#fff;text-align:center;padding-top:24px}
.cover-band .line1{font-weight:300;font-size:24px;letter-spacing:.5px}
.cover-band .line2{font-weight:700;font-size:24px;letter-spacing:.5px}
.cover-band::before{content:"";position:absolute;left:0;right:0;top:-6px;height:6px;background:var(--magenta)}

.brand{display:flex;align-items:center;gap:8px;font-weight:600;color:var(--magenta);font-size:15px;line-height:1.15}
.brand .dot{width:18px;height:18px;border-radius:50%;background:var(--blue);flex:none}
.cover .brand{position:absolute;left:24px;top:22px}

.spread{position:absolute;left:50px;width:1100px;height:367px;background:var(--paper);overflow:hidden}
.spread::after{content:"";position:absolute;left:549px;top:0;width:2px;height:100%;background:linear-gradient(90deg,rgba(0,0,0,.06),rgba(0,0,0,0))}
.page-no{position:absolute;bottom:10px;font-size:9px;color:var(--ink-light)}
.page-no::after{content:"";position:absolute;left:0;top:14px;width:46px;height:3px;background:linear-gradient(90deg,var(--magenta) 50%,var(--blue) 50%)}
.page-no.left{left:24px}.page-no.right{right:70px}

h3{font-size:10px;font-weight:700;color:var(--magenta);text-transform:uppercase;margin-bottom:3px}
p,li{font-size:9px;line-height:1.35;color:var(--ink)}
.block{position:absolute}
.block p{margin-bottom:10px}
ul.ticks{list-style:none}
ul.ticks li{position:relative;padding-left:12px;margin-bottom:3px}
ul.ticks li::before{content:"";position:absolute;left:0;top:4px;width:5px;height:5px;border-radius:50%;background:var(--blue)}

.intro{left:40px;top:80px;width:180px;font-weight:300;font-size:15px;line-height:1.3;color:var(--ink-light)}
.intro span{display:block;margin-bottom:48px}

table.data{border-collapse:collapse;width:100%;font-size:8px}
table.data th{background:var(--blue);color:#fff;font-weight:600;padding:4px 5px;text-align:left}
table.data td{padding:4px 5px;border-bottom:1px solid var(--rule);color:var(--ink)}
table.data tr:nth-child(even) td{background:#f4f6f8}
.data-label{position:absolute;top:30px;writing-mode:vertical-rl;transform:rotate(180deg);font-size:12px;letter-spacing:2px;color:var(--rule);font-weight:700}

.back-left .addr{position:absolute;left:200px;top:270px}
.addr h4{font-size:12px;font-weight:700;color:var(--magenta);line-height:1.2}
.addr p{font-size:11px;color:var(--ink-light);line-height:1.3;margin-top:4px}
.directions{position:absolute;left:550px;top:0;width:550px;height:367px;background:linear-gradient(135deg,var(--blue),var(--blue-dark));color:#fff;padding:28px 60px}
.directions h2{font-size:16px;font-weight:700;margin-bottom:10px}
.directions h5{font-size:10px;font-weight:700;margin-top:6px}
.directions p{font-size:9.5px;color:#fff;line-height:1.35}
</style>
</head>
<body>

<section class="cover">
  <div class="photo beach" role="img" aria-label="Photo of smiling senior couples walking on a beach"></div>
  <div class="brand"><span class="dot"></span>Harborview Renal<br>Dialysis</div>
  <div class="cover-tag">THIS CENTER IS A<strong>GIFT OF LIFE</strong></div>
  <div class="cover-band">
    <div class="line1">HARBORVIEW RENAL CARE CENTER</div>
    <div class="line2">DIALYSIS FACILITY</div>
  </div>
</section>

<section class="spread" style="top:607px">
  <div class="block intro">
    <span>HRCC Dialysis is a 62-Station state-of-the-art facility.</span>
    <span>The Largest Independent Dialysis Center in The United States.</span>
  </div>
  <div class="brand" style="position:absolute;left:330px;top:160px">
    <span class="dot"></span>Harborview Renal<br>Dialysis
  </div>
  <div class="photo" style="left:550px;top:0;width:550px;height:367px" role="img" aria-label="Photo of the bright dialysis treatment hall with nurse station and chairs"></div>
  <svg style="position:absolute;left:550px;top:300px" width="550" height="67" viewBox="0 0 550 67"><polygon points="0,67 0,40 550,0 550,6 12,67" fill="#2f9fe0"/></svg>
  <div class="page-no left">02</div>
</section>

<section class="spread" style="top:1074px">
  <div class="photo" style="left:0;top:0;width:300px;height:367px" role="img" aria-label="Photo of a row of treatment chairs with wall mounted TV screens"></div>
  <div class="block" style="left:330px;top:90px;width:190px">
    <h3>Regular Shifts</h3>
    <p>Monday / Wednesday / Friday or<br>Tuesday / Thursday / Saturday</p>
    <h3>Early Morning Shifts</h3>
    <p>as early as 5AM</p>
    <h3>Late Afternoon Shifts</h3>
    <p>after 5PM</p>
  </div>
  <div class="block" style="left:590px;top:60px;width:170px">
    <h3>Doctor's Services</h3>
    <ul class="ticks">
      <li>Full time nephrology staff physician on premises</li>
      <li>12 Board Certified Nephrologists</li>
      <li>You may keep your current nephrologist when you transfer to our Center</li>
    </ul>
  </div>
  <div class="photo" style="left:800px;top:0;width:300px;height:367px" role="img" aria-label="Photo of a nurse attending a patient in a treatment chair"></div>
  <div class="page-no left">04</div>
</section>

<section class="spread" style="top:1541px">
  <div class="block" style="left:40px;top:150px;width:200px">
    <h3>Accommodations</h3>
    <ul class="ticks">
      <li>All Dialysis chairs are with Heat and Massage functions</li>
      <li>Large 19" Flat screen TV with Cable TV for each station</li>
      <li>Individual tablets are available for patients use during treatment</li>
      <li>Wi-Fi High Speed Internet</li>
      <li>Multilingual Staff: Assistance with Spanish, Russian, Chinese and other languages</li>
    </ul>
  </div>
  <div class="photo round" style="left:270px;top:110px;width:110px;height:110px" role="img" aria-label="Photo of a grey treatment recliner"></div>
  <div class="photo warm" style="left:390px;top:0;width:460px;height:367px" role="img" aria-label="Photo of the waiting lounge with rows of grey chairs"></div>
  <div class="photo round" style="left:820px;top:100px;width:120px;height:120px;background:linear-gradient(160deg,#b9d6a8,#6f9a62)" role="img" aria-label="Photo of the outdoor terrace with trees"></div>
  <div class="block" style="left:900px;top:50px;width:170px">
    <ul class="ticks">
      <li>Separate extended stay Lounge Waiting Room for relatives and caregivers</li>
      <li>Outdoor Terrace with view of the marina</li>
    </ul>
  </div>
  <div class="page-no left">06</div>
  <div class="page-no right">07</div>
</section>

<section class="spread" style="top:2008px">
  <div class="block" style="left:40px;top:60px;width:200px">
    <h3>Patient Survival Rate</h3>
    <p>HRCC had the Lowest Mortality Rate (higher survival) in New York State for 2011-2017 years – 11.7 (per 100 patients)</p>
    <h3>Medicare Rating:</h3>
    <p>HRCC received 5-Star rating 9 times out of the last 10 years. Only 15% of Dialysis Centers in the United States receive 5-Star rating in any particular year.</p>
    <h3>Patient Safety Program:</h3>
    <p>5-Diamond Award – 2016, 2017, 2018. Every single year starting 2016 when this program was established</p>
  </div>
  <div class="photo" style="left:270px;top:0;width:280px;height:367px" role="img" aria-label="Photo of a nurse in blue scrubs talking with a patient"></div>
  <div class="block" style="left:590px;top:30px;width:470px">
    <table class="data">
      <tr><th>Indicator</th><th>HRCC</th><th>Nationwide</th><th>Average</th></tr>
      <tr><td>Quality of Care</td><td>5-Star</td><td>Excellent</td><td>3 - 4</td></tr>
      <tr><td>Mortality Rate (per 100 patients, lower is better)</td><td>12.7</td><td>Better than expected</td><td>17.4</td></tr>
      <tr><td>Infection Rate (lower is better)</td><td>0.24</td><td>Better than expected</td><td>1.01</td></tr>
      <tr><td>Blood Transfusions (per 100 patients)</td><td>11.6</td><td>Better than expected</td><td>39.2</td></tr>
      <tr><td>Blood waste removal rate (higher is better)</td><td>96.3%</td><td>As expected</td><td>95.9%</td></tr>
      <tr><td>Hospitalizations Rate (lower is better)</td><td>161.2</td><td>Better than expected</td><td>183.2</td></tr>
    </table>
    <p style="margin-top:8px">Over the last ten years, HRCC outperformed every other dialysis facility in the area:</p>
    <ul class="ticks">
      <li>The higher survival rate for our patients</li>
      <li>The lower infection incidents rate</li>
      <li>The most efficiency of removal waste from blood</li>
      <li>The higher patient satisfaction rate</li>
    </ul>
  </div>
  <div class="data-label" style="left:564px">2018 DATA</div>
  <div class="page-no left">08</div>
  <div class="page-no right">09</div>
</section>

<section class="spread" style="top:2475px">
  <div class="photo" style="left:0;top:0;width:270px;height:367px" role="img" aria-label="Photo of staff and patients in the treatment hall"></div>
  <div class="block" style="left:300px;top:60px;width:210px">
    <h3>Kidney Transplant Program</h3>
    <p>Every patient of HRCC who is interested in kidney transplant will be evaluated by Transplant Team Specialists.</p>
    <p>Harborview Renal Care Center is affiliated with the following University Hospital transplant programs:</p>
    <h3>Plant Programs:</h3>
    <ul class="ticks">
      <li>Eastbridge University Hospital</li>
      <li>Northgate Medical Center</li>
      <li>Lakeside Health Center</li>
      <li>Summit Valley Medical Center</li>
      <li>Riverton College of Medicine</li>
    </ul>
  </div>
  <div class="block" style="left:590px;top:50px;width:200px">
    <h3>Social Worker Services</h3>
    <ul class="ticks">
      <li>Assisting with keeping or obtaining insurance coverage</li>
      <li>Locate and access community resources</li>
      <li>Apply and obtain financial assistance, Medicaid</li>
      <li>Arrange transportation</li>
      <li>Home care services</li>
      <li>Physical, Occupational and Speech therapies</li>
      <li>Coordinate dialysis and work schedule</li>
      <li>Vocational Rehabilitation</li>
      <li>Arrange dialysis while you travel</li>
      <li>Professional counseling to patients and family</li>
    </ul>
  </div>
  <div class="photo" style="left:810px;top:0;width:290px;height:367px" role="img" aria-label="Photo of a physician in a white coat beside dialysis machines"></div>
  <div class="page-no left">10</div>
</section>

<section class="spread back-left" style="top:2942px">
  <div class="photo map" style="left:0;top:0;width:550px;height:210px" role="img" aria-label="Street map showing the center's location near the parkway"></div>
  <svg style="position:absolute;left:235px;top:70px" width="24" height="32" viewBox="0 0 24 32" aria-hidden="true"><path d="M12 0C5.4 0 0 5.4 0 12c0 9 12 20 12 20s12-11 12-20C24 5.4 18.6 0 12 0z" fill="#2f9fe0"/><circle cx="12" cy="12" r="5" fill="#fff"/></svg>
  <div class="brand" style="position:absolute;left:40px;top:270px"><span class="dot"></span>Harborview Renal<br>Dialysis</div>
  <div class="addr">
    <h4>HARBORVIEW RENAL<br>CARE CENTER</h4>
    <p>1450 Harbor Lane,<br>Brooklyn, NY 11299</p>
    <p>(555) 014-2730<br>info@harborviewrenal.example</p>
  </div>
  <div class="directions">
    <h2>Directions:</h2>
    <h5>By Public transportation:</h5>
    <p>Take H2 bus to Pier 8 Street. The entrance is on Pier 7 Street and Harbor Lane.</p>
    <h5>By Car:<br>From Manhattan and Staten Island</h5>
    <p>Take Bayline Parkway East to exit 9a (Marlow St/Gull Bay). Take the first available right turn onto Dorsey St. Make a Right onto Harbor Lane. Proceed on Harbor Lane. The dialysis unit is on the right side between Pier 7 and Pier 8 Street. The entrance is on Pier 7 Street.</p>
    <h5>From Queens or Long Island</h5>
    <p>Take Bayline Parkway West to exit 9 (Marlow St/Gull Bay). Make a left at Marlow St, then right onto Harbor Lane. Proceed on Harbor Lane. The dialysis unit is on the right side between Pier 7 and Pier 8 Street. The entrance is on Pier 7 Street.</p>
  </div>
</section>

</body>
</html>
```